Web Design Project

We are looking for a beautiful, clean web page design for our new web service: Quendara. The idea behind quendara is simple. People tell us where they live and what they love, and we point them towards interesting offers, places and events near them - as reviewed by our experts and their friends. It is available on the web and by phone. We have chosen our logo and know the elements we want on each page. Now we just need a whole a great design to pull it all together.
///
QuenDara
locate, explore and discover the best of your city with quendara
Discover your cities hottest offers
places & venues while sharing
the things that mean the most to you.
Join for free today!
//
Note: we have also had some feedback that the name is difficult to read/pronounce, so we might want to change the color of the word be in quendara so that it stands out. suggestions welcome.
Target Market(s)
Young, urban, savvy consumers
We are looking at this site for inspiration
https://trivenko.example/
elements: blog:latest news, top picks // members area // categories: fashion & beauty; food & drink; entertainment & events
Industry/Entity Type
Events
Look and feel

```html
<!DOCTYPE html>
<html lang="en">
<head>
<meta charset="utf-8">
<title>quendara – locate, explore and discover</title>
<link rel="stylesheet" href="https://fonts.googleapis.com/css2?family=Comfortaa:wght@400;700&family=Arimo:wght@400&display=swap">
<style>
:root{
  --ink:#444444;
  --ink-dark:#3a3a3a;
  --purple:#5b2a86;
  --orange:#f26b1d;
  --teal:#0f9bb3;
  --button:#3b5aa0;
  --peach:#fde0d3;
  --mist:#e4f4f5;
  --white:#ffffff;
  --photo-a:#b44a3a;
  --photo-b:#3b2a2a;
}
*{margin:0;padding:0;box-sizing:border-box}
html,body{width:1200px;height:1072px;overflow:hidden;background:var(--white)}
body{font-family:'Arimo',Arial,sans-serif;color:var(--ink);position:relative}
a{color:var(--purple);text-decoration:none}
.round{font-family:'Comfortaa',sans-serif}
.page{position:absolute;left:158px;top:0;width:891px;height:1072px}

.brand{position:absolute;left:0;top:102px;display:flex;align-items:center;gap:10px}
.brand-mark{width:14px;height:14px;background:var(--orange)}
.brand-name{font-family:'Comfortaa',sans-serif;font-size:36px;color:var(--ink)}
.tagline{position:absolute;right:0;top:70px;font-size:19px;color:var(--ink)}
.account{position:absolute;right:0;top:129px;font-size:16px;color:var(--ink)}

.nav{position:absolute;left:0;top:152px;width:891px;height:66px;background:var(--ink);border-radius:10px}
.nav a{position:absolute;top:18px;font-family:'Comfortaa',sans-serif;font-size:21px;color:var(--white)}

.discover-tail{position:absolute;left:64px;top:216px}
.discover{position:absolute;left:100px;top:221px;font-size:18px}
.discover b{font-weight:700}

.region-title{position:absolute;left:15px;top:286px;font-size:31px;color:var(--ink)}
.city-photo{position:absolute;left:12px;top:323px;width:140px;height:150px;border-radius:8px;background:linear-gradient(160deg,#e87c8c 0%,#6a4a7a 40%,#1d1d33 100%)}
.city-links{position:absolute;left:168px;top:324px;width:263px;height:148px;background:var(--peach);border-radius:8px;padding:10px 11px}
.city-links dt{font-size:15px;margin-top:9px}
.city-links dt:first-child{margin-top:0}
.city-links dd{font-size:13.5px;line-height:17px}

.hero-bubble{position:absolute;left:440px;top:200px}
.hero-copy{position:absolute;left:492px;top:224px;width:380px;font-size:21px;line-height:28px;color:var(--white)}
.hero-actions{position:absolute;left:493px;top:319px;display:flex;align-items:center;gap:8px}
.btn-social{background:var(--button);color:var(--white);font-family:'Comfortaa',sans-serif;font-size:16px;padding:7px 11px;border:1px solid #2b4580}
.hero-actions small{font-size:13px;color:var(--ink)}
.hero-actions .register{font-size:17px;color:var(--white)}

.hot{position:absolute;left:0;top:489px;width:891px;height:456px;background:var(--mist);border-radius:10px}
.hot h2{position:absolute;left:15px;top:17px;font-family:'Comfortaa',sans-serif;font-weight:400;font-size:20px}
.zone{position:absolute;top:75px;width:210px}
.zone h3{font-family:'Comfortaa',sans-serif;font-weight:400;font-size:16px;margin-bottom:22px}
.pick{display:flex;gap:6px;height:109px}
.pick-photo{width:80px;height:80px;flex:none;border-radius:6px;background:radial-gradient(circle at 40% 45%,var(--photo-a),var(--photo-b))}
.pick-info{font-size:14px;line-height:15.5px;margin-top:-3px}
.pick-info a{display:block}
.pick-info time{display:block;font-size:11px;color:#666}

.footer{position:absolute;left:0;top:962px;width:891px;height:82px;background:var(--peach);border-radius:10px;font-size:13.5px}
.footer .copy{position:absolute;left:15px;top:34px}
.footer nav{position:absolute;left:478px;top:33px}
</style>
</head>
<body>
<div class="page">
  <header>
    <div class="brand"><span class="brand-mark"></span><span class="brand-name">quendara</span></div>
    <p class="tagline round">locate, explore and discover the best of your city</p>
    <p class="account">already registered? <a href="#">Login</a></p>
  </header>

  <nav class="nav">
    <a href="#" style="left:53px">home</a>
    <a href="#" style="left:161px">blog</a>
    <a href="#" style="left:251px">members area</a>
    <a href="#" style="left:453px">categories</a>
  </nav>

  <svg class="discover-tail" width="40" height="74" viewBox="0 0 40 74"><path d="M0 0 H34 Q26 30 22 72 Q8 30 0 0Z" fill="var(--ink)"/></svg>
  <p class="discover round">what will you <b>discover</b> today?</p>

  <h1 class="region-title round" style="font-weight:400">australia</h1>
  <div class="city-photo" role="img" aria-label="City harbour skyline at dusk"></div>
  <dl class="city-links">
    <dt>food &amp; drink, in</dt>
    <dd><a href="#">sydney</a> I <a href="#">melbourne</a> I <a href="#">brisbane</a> I <a href="#">perth</a></dd>
    <dt>entertainment &amp; events, in</dt>
    <dd><a href="#">sydney</a> I <a href="#">melbourne</a> I <a href="#">brisbane</a> I <a href="#">perth</a></dd>
    <dt>fashion &amp; beauty, in</dt>
    <dd><a href="#">sydney</a> I <a href="#">melbourne</a> I <a href="#">brisbane</a> I <a href="#">perth</a></dd>
  </dl>

  <svg class="hero-bubble" width="452" height="294" viewBox="0 0 452 294">
    <path d="M0 0 H450 V110 Q450 160 400 161 H248 Q238 230 226 292 Q214 220 190 161 H60 Q0 160 0 100Z" fill="var(--teal)"/>
  </svg>
  <p class="hero-copy round">Discover your cities hottest offers places &amp; venues while sharing the things that mean the most to you.</p>
  <div class="hero-actions">
    <a class="btn-social" href="#">login with circlenet</a>
    <small>not on circlenet?</small>
    <a class="register round" href="#">register</a>
  </div>

  <section class="hot">
    <h2>what’s hot today?</h2>

    <div class="zone" style="left:15px">
      <h3>north america</h3>
      <div class="pick"><div class="pick-photo" role="img" aria-label="Guests at a lively venue"></div><div class="pick-info">dining<a href="#">Los angeles</a><a href="#">Food &amp; drink</a><time>At 18:59 29/11/11</time></div></div>
      <div class="pick"><div class="pick-photo" role="img" aria-label="Guests at a lively venue"></div><div class="pick-info">shopping<a href="#">Chicago</a><a href="#">Fashion &amp; Beauty</a><time>At 18:59 29/11/11</time></div></div>
      <div class="pick"><div class="pick-photo" role="img" aria-label="Guests at a lively venue"></div><div class="pick-info">festival<a href="#">Boston</a><a href="#">Entertainment &amp; Events</a><time>At 18:59 29/11/11</time></div></div>
    </div>

    <div class="zone" style="left:232px">
      <h3>europe</h3>
      <div class="pick"><div class="pick-photo" role="img" aria-label="Guests at a lively venue"></div><div class="pick-info">shopping<a href="#">Paris</a><a href="#">Fashion &amp; Beauty</a><time>At 18:59 29/11/11</time></div></div>
      <div class="pick"><div class="pick-photo" role="img" aria-label="Guests at a lively venue"></div><div class="pick-info">dining<a href="#">Venice</a><a href="#">Food &amp; drink</a><time>At 18:59 29/11/11</time></div></div>
      <div class="pick"><div class="pick-photo" role="img" aria-label="Guests at a lively venue"></div><div class="pick-info">theatre<a href="#">London</a><a href="#">Entertainment &amp; Events</a><time>At 18:59 29/11/11</time></div></div>
    </div>

    <div class="zone" style="left:449px">
      <h3>asia</h3>
      <div class="pick"><div class="pick-photo" role="img" aria-label="Guests at a lively venue"></div><div class="pick-info">dining<a href="#">Bangkok</a><a href="#">Food &amp; drink</a><time>At 18:59 29/11/11</time></div></div>
      <div class="pick"><div class="pick-photo" role="img" aria-label="Guests at a lively venue"></div><div class="pick-info">festival<a href="#">Kuala Lumpur</a><a href="#">Entertainment &amp; Events</a><time>At 18:59 29/11/11</time></div></div>
      <div class="pick"><div class="pick-photo" role="img" aria-label="Guests at a lively venue"></div><div class="pick-info">shopping<a href="#">Tokyo</a><a href="#">Fashion &amp; Beauty</a><time>At 18:59 29/11/11</time></div></div>
    </div>

    <div class="zone" style="left:666px">
      <h3>australia &amp; nz</h3>
      <div class="pick"><div class="pick-photo" role="img" aria-label="Guests at a lively venue"></div><div class="pick-info">live band<a href="#">Sydney</a><a href="#">Entertainment &amp; Events</a><time>At 18:59 29/11/11</time></div></div>
      <div class="pick"><div class="pick-photo" role="img" aria-label="Guests at a lively venue"></div><div class="pick-info">shopping<a href="#">Sydney</a><a href="#">Fashion &amp; Beaty</a><time>At 18:59 29/11/11</time></div></div>
      <div class="pick"><div class="pick-photo" role="img" aria-label="Guests at a lively venue"></div><div class="pick-info">dining<a href="#">Melbourne</a><a href="#">Food &amp; drink</a><time>At 18:59 29/11/11</time></div></div>
    </div>
  </section>

  <footer class="footer">
    <p class="copy">quendara © 2011</p>
    <nav><a href="#">Home</a> I <a href="#">Blog</a> I <a href="#">Members</a> I <a href="#">Area</a> I <a href="#">Categories</a> I <a href="#">About</a> I <a href="#">Contact</a></nav>
  </footer>
</div>
</body>
</html>
```